Alternative Health business needs a self help book cover design

Silver Brook Wellness requires an E book and print cover design for a new self help book titled "Making The Bright Choice". Sub title 'Ways to shape the bright days YOU seek' . Author Danica Forworth. The book is about deliberately changing things now, so you feel happy now and this then flows out an effects everything else in your life. It combines NLP, yoga philosophy and modern psychology in a down to earth, easy to read manner. I would like the cover to be happy, colourful, beautiful, artistic and hip. Maybe something hand drawn or painted. Something a woman would want to display and something that makes you smile and feel happy.
I don't want it to look like a romance novel and would prefer no photos of people. Pics are of other peoples covers I like. Thank you in advance. danica

Target Market(s)

woman 18-50

Industry/Entity Type

Business

Requirements
Must have
• happy feeling. professional look
Nice to have
• original drawing or painting
Should not have
• photos of real people, yellow smiley faces, sunsets, butterflies, yoga, tree, elements of my business logo

```html
<!DOCTYPE html>
<html lang="en">
<head>
<meta charset="utf-8">
<title>Making The Bright Choice – Danica Forworth</title>
<link rel="stylesheet" href="https://fonts.googleapis.com/css2?family=Caveat:wght@500&family=Cinzel+Decorative:wght@400;700&family=Cinzel:wght@400&display=swap">
<style>
  :root {
    --paper: #f7f6ef;
    --paper-mid: #e4e6e0;
    --edge: #5d7a8c;
    --edge-deep: #3f5f73;
    --ink-title: #1f5a6e;
    --ink-sub: #4a4c4e;
    --ink-author: #2b4653;
    --title-shadow: rgba(120, 120, 110, 0.45);
    --candy-red: #e5322c;
    --candy-orange: #f59a1f;
    --candy-yellow: #f3e23a;
    --candy-green: #6dbe45;
    --candy-blue: #3bb3e6;
  }
  html, body {
    margin: 0;
    padding: 0;
    width: 800px;
    height: 1200px;
    overflow: hidden;
  }
  .cover {
    position: relative;
    width: 800px;
    height: 1200px;
    overflow: hidden;
    background:
      radial-gradient(ellipse 70% 62% at 50% 52%, var(--paper) 0%, var(--paper) 45%, var(--paper-mid) 70%, var(--edge) 100%),
      var(--edge-deep);
  }
  .cover::after {
    content: "";
    position: absolute;
    inset: 0;
    background: linear-gradient(to bottom, rgba(63, 95, 115, 0.35) 0%, rgba(63, 95, 115, 0) 18%, rgba(63, 95, 115, 0) 85%, rgba(63, 95, 115, 0.3) 100%);
    pointer-events: none;
  }
  .subtitle {
    position: absolute;
    top: 58px;
    left: 0;
    width: 800px;
    margin: 0;
    text-align: center;
    font-family: "Caveat", cursive;
    font-weight: 500;
    font-size: 48px;
    line-height: 60px;
    color: var(--ink-sub);
    letter-spacing: 1px;
  }
  .candy-art {
    position: absolute;
    left: 92px;
    top: 409px;
    width: 254px;
    height: 254px;
    border-radius: 18px;
    background:
      radial-gradient(circle at 50% 50%, rgba(243, 226, 58, 0.55) 0%, rgba(243, 226, 58, 0) 55%),
      linear-gradient(135deg, var(--candy-red) 0%, var(--candy-orange) 30%, var(--candy-green) 65%, var(--candy-blue) 100%);
    opacity: 0.85;
  }
  .title {
    margin: 0;
    font-family: "Cinzel Decorative", serif;
    font-weight: 400;
    color: var(--ink-title);
  }
  .title span {
    position: absolute;
    display: block;
    white-space: nowrap;
    line-height: 1;
    text-shadow: 5px 4px 0 var(--title-shadow);
  }
  .title-word-1 { top: 258px; left: 66px; font-size: 104px; }
  .title-word-2 { top: 378px; left: 440px; font-size: 48px; }
  .title-word-3 { top: 440px; left: 370px; font-size: 108px; }
  .title-word-4 { top: 690px; left: 78px; font-size: 140px; font-weight: 700; }
  .author {
    position: absolute;
    top: 1100px;
    left: 0;
    width: 800px;
    margin: 0;
    text-align: center;
    font-family: "Cinzel", serif;
    font-weight: 400;
    font-size: 46px;
    letter-spacing: 3px;
    color: var(--ink-author);
  }
</style>
</head>
<body>
<main class="cover">
  <p class="subtitle">Ways to shape<br>the bright days YOU seek</p>

  <div class="candy-art" role="img" aria-label="Rainbow swirl lollipop whose stick ends in a green key"></div>

  <h1 class="title">
    <span class="title-word-1">Making</span>
    <span class="title-word-2">The</span>
    <span class="title-word-3">Bright</span>
    <span class="title-word-4">Choice</span>
  </h1>

  <p class="author">Danica Forworth</p>
</main>
</body>
</html>
```